Professional Commercial Cleaning Business needing fresh professional designs for stationary

Need highly professional templates to make our commercial presentations, proposals and tenders standout from the crowd.

We provide cleaning services to large multi national companies. We need to look as professional as our clients and partners.

Needed:
- Word Templates, Cover and main pages
- Power point Templates, Cover and main pages
- Letter Head template
- Header template
- Footer template

Reason: Still waiting on other designed from different designers.

Target Market(s)

Large multi-national companies

Industry/Entity Type

Commercial

Font styles to use
Sans Serif

Colors
3276b5
abd036
cfdeed
85abd2
eaf2ce

Requirements
Must have
• Please see brief for what we need specifically.
• Show our logo
• Use QAB logos

```html
<!DOCTYPE html>
<html lang="en">
<head>
<meta charset="utf-8">
<title>Brightway Cleaning Services – Stationery</title>
<link rel="stylesheet" href="https://fonts.googleapis.com/css2?family=Open+Sans:wght@400;600;700&display=swap">
<style>
  :root{
    --blue:#3276b5;
    --blue-mid:#85abd2;
    --blue-pale:#cfdeed;
    --green:#abd036;
    --green-deep:#6fa01e;
    --green-pale:#eaf2ce;
    --ink:#2b2b2b;
    --muted:#6b6b6b;
    --paper:#ffffff;
    --stage:#d9d9d9;
    --stage-light:#ececec;
  }
  *{box-sizing:border-box;margin:0;padding:0}
  html,body{width:1200px;height:5263px;overflow:hidden}
  body{position:relative;background:var(--paper);font-family:"Open Sans",Arial,sans-serif;color:var(--ink)}

  .section{position:absolute;left:0;width:1200px}
  .section--intro{top:0;height:245px;background:var(--paper)}
  .section--documents{top:245px;height:1740px;background:var(--stage)}
  .section--envelopes{top:2020px;height:790px;background:var(--stage)}
  .section--letterhead{top:2865px;height:1155px;background:var(--stage-light)}
  .section--suite{top:4053px;height:1210px;background:var(--stage)}

  /* brand lockup */
  .brand{display:flex;align-items:center;gap:.45em;color:var(--blue);font-weight:700;line-height:1}
  .brand__dot{width:1.5em;height:1.5em;border-radius:50%;background:var(--green);flex:none}
  .brand__name{display:flex;flex-direction:column;gap:.12em}
  .brand__name span:last-child{font-size:.42em;letter-spacing:.08em;text-transform:uppercase}
  .brand--hero{font-size:48px;position:absolute;left:50%;top:70px;transform:translateX(-50%)}

  /* sheet with waves */
  .sheet{position:absolute;background:var(--paper);overflow:hidden;box-shadow:0 2px 6px rgba(0,0,0,.15)}
  .waves{position:absolute;inset:0;width:100%;height:100%}
  .w-blue-lt{fill:var(--blue-mid)}
  .w-blue{fill:var(--blue)}
  .w-green-lt{fill:var(--green-pale)}
  .w-green{fill:var(--green)}
  .w-green-dk{fill:var(--green-deep)}

  .sheet--cover{left:140px;top:175px;width:913px;height:737px}
  .sheet--cover .brand{font-size:52px;position:absolute;left:50%;top:46%;transform:translate(-50%,-50%)}

  /* certificate */
  .sheet--certificate{left:140px;top:965px;width:913px;height:685px}
  .cert .brand{font-size:26px;position:absolute;left:120px;top:58px}
  .cert__seal{position:absolute;right:150px;top:50px;width:86px;height:86px;border-radius:50%;border:3px solid #555;background:var(--paper)}
  .cert__head{position:absolute;left:0;right:0;top:70px;text-align:center}
  .cert__kicker{font-size:14px;color:var(--ink)}
  .cert__title{font-size:32px;font-weight:700;color:var(--ink);line-height:1.1}
  .cert__line{font-size:13px;margin-top:4px}
  .cert__company{font-size:22px;font-weight:700;margin:10px 0 2px}
  .cert__std{font-size:26px;font-weight:700;margin-top:12px}
  .cert__std-note{font-size:10px;color:var(--muted)}
  .cert__grid{position:absolute;left:120px;right:90px;top:400px;display:grid;grid-template-columns:1fr 1fr;gap:30px 40px;font-size:11px}
  .cert__grid b{display:block;font-size:12px}
  .cert__sign{border-top:1px solid #777;padding-top:6px;width:190px;margin-left:auto}
  .cert__badges{position:absolute;right:90px;bottom:60px;display:flex;gap:14px}
  .badge{width:64px;height:42px;background:#e3e3e3;border-radius:3px}
  .badge--round{width:42px;border-radius:50%;background:#c9a94a}
  .badge--blue{background:var(--blue)}

  /* envelopes */
  .sheet--env-front{left:140px;top:50px;width:955px;height:210px}
  .sheet--env-back{left:140px;top:366px;width:955px;height:228px}
  .sheet--env-front .brand{font-size:30px;position:absolute;left:110px;top:72px}
  .address{position:absolute;font-size:19px;line-height:1.25;color:var(--ink)}
  .sheet--env-front .address{left:600px;top:88px}
  .contact{position:absolute;font-size:17px;font-weight:600;line-height:1.45}
  .sheet--env-back .contact{left:600px;top:60px}

  /* letterhead */
  .sheet--letter{left:298px;top:100px;width:755px;height:965px}
  .letter .brand{font-size:26px;position:absolute;left:100px;top:115px}
  .letter .address{right:60px;top:118px;font-size:17px;font-weight:600;text-align:left}
  .letter__body{position:absolute;left:100px;right:80px;top:220px;font-size:11.5px;line-height:1.6;color:var(--muted)}
  .letter__body p{margin-bottom:70px}
  .letter__signoff{position:absolute;right:80px;top:660px;font-size:13px;color:var(--muted)}
  .letter .contact{right:80px;top:730px;font-size:14px;text-align:right}

  /* stationery suite */
  .suite .sheet .brand{font-size:12px;position:absolute;left:10%;top:30%}
  .suite .contact{font-size:8px;right:8%;bottom:14%;text-align:right}
  .env-a{left:70px;top:57px;width:360px;height:150px}
  .env-b{left:70px;top:247px;width:360px;height:150px}
  .card-a{left:470px;top:87px;width:220px;height:125px}
  .card-b{left:470px;top:247px;width:220px;height:125px}
  .card-c{left:470px;top:417px;width:220px;height:125px}
  .dl{left:470px;top:577px;width:220px;height:120px}
  .dl__window{position:absolute;left:38%;top:40%;width:48%;height:26%;border:1px solid #ccc;border-radius:4px;background:#f4f4f4}
  .page-a{left:780px;top:57px;width:300px;height:400px}
  .page-b{left:780px;top:497px;width:300px;height:400px}
  .cert-mini{left:70px;top:447px;width:360px;height:250px}
  .cert-mini .brand{top:10%}
  .cert-mini__title{position:absolute;left:0;right:0;top:32%;text-align:center;font-size:16px;font-weight:700}
  .cert-mini__lines{position:absolute;left:18%;right:18%;top:48%;height:30%;background:repeating-linear-gradient(#ddd 0 2px,transparent 2px 10px)}
  .disc{position:absolute;left:100px;top:747px;width:260px;height:260px;border-radius:50%;background:var(--paper);box-shadow:0 2px 6px rgba(0,0,0,.15);overflow:hidden}
  .disc::before{content:"";position:absolute;left:-10%;right:-10%;bottom:-5%;height:45%;background:var(--green);border-radius:50% 50% 0 0}
  .disc::after{content:"";position:absolute;left:50%;top:50%;width:50px;height:50px;margin:-25px;border-radius:50%;background:var(--stage);border:6px solid #eee}
  .folder{left:470px;top:747px;width:260px;height:380px}
  .notebook{left:780px;top:937px;width:300px;height:240px}
  .suite .page-a .brand,.suite .page-b .brand{font-size:14px;top:10%}
  .suite .page-b .brand{top:46%;left:30%}
  .suite .folder .brand{font-size:16px;top:40%;left:20%}
  .suite .notebook .brand{font-size:14px;top:40%;left:30%}
</style>
</head>
<body>

<section class="section section--intro">
  <div class="brand brand--hero"><span class="brand__dot"></span><span class="brand__name"><span>Brightway</span><span>Cleaning Services</span></span></div>
</section>

<section class="section section--documents">
  <article class="sheet sheet--cover">
    <svg class="waves" viewBox="0 0 100 100" preserveAspectRatio="none" aria-hidden="true"><path class="w-blue-lt" d="M52 0H100V30C90 12 74 3 52 0Z"/><path class="w-blue" d="M64 0H100V22C92 9 80 3 64 0Z"/><path class="w-green-lt" d="M0 70C18 74 34 86 42 100H0Z"/><path class="w-green" d="M0 78C16 80 27 90 34 100H0Z"/><path class="w-green-dk" d="M0 90C10 91 18 95 22 100H0Z"/></svg>
    <div class="brand"><span class="brand__dot"></span><span class="brand__name"><span>Brightway</span><span>Cleaning Services</span></span></div>
  </article>

  <article class="sheet sheet--certificate cert">
    <svg class="waves" viewBox="0 0 100 100" preserveAspectRatio="none" aria-hidden="true"><path class="w-blue-lt" d="M60 0H100V26C90 11 78 3 60 0Z"/><path class="w-blue" d="M70 0H100V18C92 8 82 3 70 0Z"/><path class="w-green-lt" d="M0 80C16 82 28 90 34 100H0Z"/><path class="w-green" d="M0 86C12 87 20 93 25 100H0Z"/></svg>
    <div class="brand"><span class="brand__dot"></span><span class="brand__name"><span>Brightway</span><span>Cleaning Services</span></span></div>
    <div class="cert__seal"></div>
    <div class="cert__head">
      <p class="cert__kicker">Certificate Of</p>
      <p class="cert__title">Registration</p>
      <p class="cert__line">This is to certify that the management system of</p>
      <p class="cert__company">Brightway Cleaning Services</p>
      <p class="cert__line">Have been formally assessed by Northgate Assurance Board<br>&amp; found to comply with the requirements of</p>
      <p class="cert__std">QAB 14001:2015</p>
      <p class="cert__std-note">Environmental Management Systems Requirements with guidance for use</p>
    </div>
    <div class="cert__grid">
      <div><b>Scope of Registration</b>Construction, Commercial, Industrial &amp; Domestic Cleaning</div>
      <div><b>Registered Address</b>12/40 Ferry Street, Kingsford Vale, VIC 3105, Australia</div>
      <div><b>Issue Date : 01-May-2017</b><b>Expire Date : 05-Apr-2020</b></div>
      <div class="cert__sign"><b>Daniel R. Moore</b>Lead Registration Assessor<br>Northgate Assurance Board</div>
    </div>
    <div class="cert__badges"><span class="badge"></span><span class="badge badge--blue"></span><span class="badge badge--round"></span><span class="badge badge--blue"></span></div>
  </article>
</section>

<section class="section section--envelopes">
  <article class="sheet sheet--env-front">
    <svg class="waves" viewBox="0 0 100 100" preserveAspectRatio="none" aria-hidden="true"><path class="w-blue-lt" d="M72 0H100V60C94 26 86 6 72 0Z"/><path class="w-blue" d="M80 0H100V45C95 18 89 4 80 0Z"/></svg>
    <div class="brand"><span class="brand__dot"></span><span class="brand__name"><span>Brightway</span><span>Cleaning Services</span></span></div>
    <p class="address">48 Harbour Rd. Melbourne<br>FL 32910</p>
  </article>
  <article class="sheet sheet--env-back">
    <svg class="waves" viewBox="0 0 100 100" preserveAspectRatio="none" aria-hidden="true"><path class="w-green-lt" d="M0 40C14 46 26 72 32 100H0Z"/><path class="w-green" d="M0 56C11 60 20 80 24 100H0Z"/></svg>
    <div class="contact">+00 321 654 0987<br>info@brightwaycleaning.com<br>www.brightwaycleaning.com</div>
  </article>
</section>

<section class="section section--letterhead">
  <article class="sheet sheet--letter letter">
    <svg class="waves" viewBox="0 0 100 100" preserveAspectRatio="none" aria-hidden="true"><path class="w-blue-lt" d="M68 0H100V18C92 7 82 2 68 0Z"/><path class="w-blue" d="M76 0H100V13C94 5 86 2 76 0Z"/><path class="w-green-lt" d="M0 84C16 86 28 93 35 100H0Z"/><path class="w-green" d="M0 89C12 90 20 95 25 100H0Z"/></svg>
    <div class="brand"><span class="brand__dot"></span><span class="brand__name"><span>Brightway</span><span>Cleaning Services</span></span></div>
    <p class="address">48 Harbour Rd. Melbourne<br>FL 32910</p>
    <div class="letter__body">
      <p>We thank you for the opportunity to present our commercial cleaning proposal. Our trained teams deliver consistent, audited results for offices, warehouses and shared facilities across the region, using certified products and clear reporting so every site stays safe, healthy and presentable for staff and visitors alike.</p>
      <p>Each contract begins with a site walk and a written scope. A dedicated supervisor sets schedules, checks quality each week and keeps your facility manager informed. Our staff are screened, insured and trained in safe work methods, and every visit is logged for easy review.</p>
      <p>We would welcome the chance to discuss your needs in person. Please contact our office to arrange a meeting at a time that suits you, and we will prepare a tailored quote within five working days.</p>
    </div>
    <p class="letter__signoff">Kind regards</p>
    <div class="contact">+00 321 654 0987<br>info@brightwaycleaning.com<br>www.brightwaycleaning.com</div>
  </article>
</section>

<section class="section section--suite suite">
  <article class="sheet env-a">
    <svg class="waves" viewBox="0 0 100 100" preserveAspectRatio="none" aria-hidden="true"><path class="w-blue-lt" d="M72 0H100V60C94 26 86 6 72 0Z"/><path class="w-blue" d="M80 0H100V45C95 18 89 4 80 0Z"/></svg>
    <div class="brand"><span class="brand__dot"></span><span class="brand__name"><span>Brightway</span><span>Cleaning Services</span></span></div>
  </article>
  <article class="sheet env-b">
    <svg class="waves" viewBox="0 0 100 100" preserveAspectRatio="none" aria-hidden="true"><path class="w-green-lt" d="M0 40C14 46 26 72 32 100H0Z"/><path class="w-green" d="M0 56C11 60 20 80 24 100H0Z"/></svg>
    <div class="contact">+00 321 654 0987<br>info@brightwaycleaning.com<br>www.brightwaycleaning.com</div>
  </article>
  <article class="sheet card-a">
    <svg class="waves" viewBox="0 0 100 100" preserveAspectRatio="none" aria-hidden="true"><path class="w-blue" d="M70 0H100V40C92 16 84 4 70 0Z"/></svg>
    <div class="brand"><span class="brand__dot"></span><span class="brand__name"><span>Brightway</span><span>Cleaning Services</span></span></div>
  </article>
  <article class="sheet card-b">
    <svg class="waves" viewBox="0 0 100 100" preserveAspectRatio="none" aria-hidden="true"><path class="w-green" d="M0 60C14 64 24 80 30 100H0Z"/></svg>
    <div class="contact">+00 321 654 0987<br>info@brightwaycleaning.com</div>
  </article>
  <article class="sheet card-c">
    <svg class="waves" viewBox="0 0 100 100" preserveAspectRatio="none" aria-hidden="true"><path class="w-blue" d="M70 0H100V40C92 16 84 4 70 0Z"/><path class="w-green" d="M0 70C12 73 20 86 24 100H0Z"/></svg>
    <div class="brand"><span class="brand__dot"></span><span class="brand__name"><span>Brightway</span><span>Cleaning Services</span></span></div>
  </article>
  <article class="sheet dl">
    <svg class="waves" viewBox="0 0 100 100" preserveAspectRatio="none" aria-hidden="true"><path class="w-green" d="M0 70C12 73 20 86 24 100H0Z"/></svg>
    <span class="dl__window"></span>
  </article>
  <article class="sheet cert-mini">
    <svg class="waves" viewBox="0 0 100 100" preserveAspectRatio="none" aria-hidden="true"><path class="w-blue" d="M70 0H100V20C92 8 82 3 70 0Z"/><path class="w-green" d="M0 86C12 87 20 93 25 100H0Z"/></svg>
    <div class="brand"><span class="brand__dot"></span><span class="brand__name"><span>Brightway</span><span>Cleaning Services</span></span></div>
    <p class="cert-mini__title">Registration</p>
    <span class="cert-mini__lines"></span>
  </article>
  <article class="sheet page-a">
    <svg class="waves" viewBox="0 0 100 100" preserveAspectRatio="none" aria-hidden="true"><path class="w-blue" d="M72 0H100V15C92 6 84 2 72 0Z"/><path class="w-green" d="M0 89C12 90 20 95 25 100H0Z"/></svg>
    <div class="brand"><span class="brand__dot"></span><span class="brand__name"><span>Brightway</span><span>Cleaning Services</span></span></div>
  </article>
  <article class="sheet page-b">
    <svg class="waves" viewBox="0 0 100 100" preserveAspectRatio="none" aria-hidden="true"><path class="w-blue-lt" d="M60 0H100V24C90 10 78 3 60 0Z"/><path class="w-blue" d="M70 0H100V17C92 7 82 2 70 0Z"/><path class="w-green-lt" d="M0 76C18 79 30 89 38 100H0Z"/><path class="w-green" d="M0 84C14 86 23 93 28 100H0Z"/></svg>
    <div class="brand"><span class="brand__dot"></span><span class="brand__name"><span>Brightway</span><span>Cleaning Services</span></span></div>
  </article>
  <div class="disc" aria-hidden="true"></div>
  <article class="sheet folder">
    <svg class="waves" viewBox="0 0 100 100" preserveAspectRatio="none" aria-hidden="true"><path class="w-blue" d="M66 0H100V18C92 7 82 2 66 0Z"/><path class="w-green-lt" d="M0 78C18 80 30 90 38 100H0Z"/><path class="w-green" d="M0 86C14 87 23 94 28 100H0Z"/></svg>
    <div class="brand"><span class="brand__dot"></span><span class="brand__name"><span>Brightway</span><span>Cleaning Services</span></span></div>
  </article>
  <article class="sheet notebook">
    <svg class="waves" viewBox="0 0 100 100" preserveAspectRatio="none" aria-hidden="true"><path class="w-blue" d="M70 0H100V24C92 9 82 2 70 0Z"/><path class="w-green" d="M0 80C12 82 20 90 25 100H0Z"/></svg>
    <div class="brand"><span class="brand__dot"></span><span class="brand__name"><span>Brightway</span><span>Cleaning Services</span></span></div>
  </article>
</section>

</body>
</html>
```